Oven Cleaning Business owner needs business card design

Hi there,
Would like for a business card to be designed for myself, the owner of a professional oven cleaning business on the Sunshine Coast.
Would like it to look sleek, and modern-ish. Bit creative is encouraged too.
Include following:
Name/title: Corin de Walbrek, Owner
Phone number: 1300 482 906
Email: info@kitchenlustrely.com.au
Website: www.kitchenlustrely.com.au

```html
<!DOCTYPE html>
<html lang="en">
<head>
<meta charset="utf-8">
<title>Kitchen Lustrely – Business Card</title>
<link rel="stylesheet" href="https://fonts.googleapis.com/css2?family=Roboto:wght@400;500;700&display=swap">
<style>
  :root {
    --teal: #22c9cf;
    --black: #050505;
    --white: #fbfbfb;
    --ink: #1a1a1a;
    --muted: #8a8a8a;
    --backdrop: #d9dadb;
  }
  * { box-sizing: border-box; margin: 0; padding: 0; }
  html, body { width: 1200px; height: 874px; overflow: hidden; }
  body {
    background: var(--backdrop);
    font-family: "Roboto", Arial, sans-serif;
    position: relative;
  }
  .card {
    position: absolute;
    left: 280px;
    width: 640px;
    height: 366px;
    border-radius: 22px;
    overflow: hidden;
    box-shadow: 0 10px 28px rgba(0,0,0,0.25);
  }
  .card-back { top: 44px; background: var(--black); }
  .card-front { top: 456px; background: var(--white); }

  .brand {
    display: flex;
    align-items: center;
    gap: 14px;
    font-weight: 700;
    text-transform: uppercase;
    letter-spacing: 0.04em;
    line-height: 1;
  }
  .brand-dot {
    flex: none;
    border-radius: 50%;
    background: var(--teal);
  }
  .card-back .brand {
    position: absolute;
    left: 50%; top: 50%;
    transform: translate(-50%, -50%);
    color: var(--white);
    font-size: 44px;
    white-space: nowrap;
  }
  .card-back .brand-dot { width: 64px; height: 64px; }

  .card-front .brand {
    position: absolute;
    left: 40px; top: 150px;
    width: 228px;
    color: var(--ink);
    font-size: 26px;
    gap: 10px;
  }
  .card-front .brand-dot { width: 44px; height: 44px; }
  .brand-name { display: block; }

  .divider {
    position: absolute;
    left: 282px; top: 130px;
    width: 1px; height: 110px;
    background: var(--muted);
  }
  .contact {
    position: absolute;
    left: 300px; top: 134px;
    color: var(--ink);
  }
  .contact-name {
    color: var(--teal);
    font-size: 24px;
    font-weight: 500;
    text-transform: uppercase;
    letter-spacing: 0.01em;
  }
  .contact-title { font-size: 15px; margin: 2px 0 10px; }
  .contact-list { list-style: none; font-size: 16px; }
  .contact-list li {
    display: flex; align-items: center; gap: 10px;
    margin-bottom: 5px;
  }
  .contact-list .phone { font-size: 19px; }
  .icon { width: 14px; height: 14px; flex: none; fill: var(--teal); }

  .front-band {
    position: absolute;
    left: 0; right: 0; bottom: 0;
    height: 12px;
    display: flex;
  }
  .band-dark { flex: 0 0 66%; background: var(--black); }
  .band-teal { flex: 1; background: var(--teal); }
</style>
</head>
<body>
  <section class="card card-back">
    <div class="brand">
      <span class="brand-dot"></span>
      <span class="brand-name">Kitchen Lustrely</span>
    </div>
  </section>

  <section class="card card-front">
    <div class="brand">
      <span class="brand-dot"></span>
      <span class="brand-name">Kitchen<br>Lustrely</span>
    </div>
    <div class="divider"></div>
    <div class="contact">
      <h1 class="contact-name">Corin de Walbrek</h1>
      <p class="contact-title">Owner</p>
      <ul class="contact-list">
        <li class="phone">
          <svg class="icon" viewBox="0 0 24 24"><path d="M6.6 10.8a15 15 0 0 0 6.6 6.6l2.2-2.2a1 1 0 0 1 1-.25 11.4 11.4 0 0 0 3.6.57 1 1 0 0 1 1 1V20a1 1 0 0 1-1 1A17 17 0 0 1 3 4a1 1 0 0 1 1-1h3.5a1 1 0 0 1 1 1c0 1.25.2 2.45.57 3.57a1 1 0 0 1-.25 1z"/></svg>
          1300 482 906
        </li>
        <li>
          <svg class="icon" viewBox="0 0 24 24"><path d="M2 5h20v14H2z M2 5l10 8 10-8" fill="var(--teal)" stroke="var(--white)" stroke-width="1.6"/></svg>
          info@kitchenlustrely.com.au
        </li>
        <li>
          <svg class="icon" viewBox="0 0 24 24"><circle cx="12" cy="12" r="10"/><path d="M2 12h20M12 2c3 3 3 17 0 20M12 2c-3 3-3 17 0 20" fill="none" stroke="var(--white)" stroke-width="1.4"/></svg>
          www.kitchenlustrely.com.au
        </li>
      </ul>
    </div>
    <div class="front-band">
      <span class="band-dark"></span>
      <span class="band-teal"></span>
    </div>
  </section>
</body>
</html>
```